Web application design for investigative software

ThreadKove is an investigation web application that would organize, create visualizations and allow collaboration. It’s available to anyone and can be used by students, historians, watchdog groups, civic hackers, investigative reporters, mystery enthusiasts, authors, even conspiracy theorists.

We are looking for two related pages. The first, a splash, or front, page and the second a ‘template’ for the web application. They should both be styled the same. The only restriction is that the logo is set.

The design should also be modern and visually well organized — employing a combination of visual devices and info graphics. Keep it light and not too heavy but strong/ professional. Do not be influenced by the current colors of threadkove.example, though the colors should be compatible with the logo..

The pages should be compatible with bootstrap, mostly for it’s JS and component functionality. It can be advised by the designer that a subset of bootstrap be used.

The splash page.
Something along the lines of (though not a copy of) :
https://www.brimloft.example/advertise
http://www.palvornhosting.example/
http://www.murkelsoft.example/
http://www.vontasky.example/

I have a very rough wire frame ish html file uploaded. Use a a guide, but alternate ideas are encouraged.

The application page should have some sort of bar for at the top for system level links a header and a footer. A vertical column to the left between the header and footer for ads, though this will be dynamic as a user can pay out of seeing adds. All dynamic actions will be made by the developers at ThreadKove.

WARNING. Please do not submit pre-made templates from some template website. We can do that ourselves for free.

This project will deliver CODE. HTML, CSS and supporting graphics and files.

```html
<!DOCTYPE html>
<html lang="en">
<head>
<meta charset="utf-8">
<title>ThreadKove — Track, Relate, Investigate</title>
<link rel="stylesheet" href="https://fonts.googleapis.com/css2?family=Open+Sans:wght@300;400;600;700&display=swap">
<style>
  :root {
    --red: #d9261c;
    --red-dark: #b81d15;
    --blue: #1ea7e1;
    --ink: #333333;
    --text: #6b6b6b;
    --muted: #9a9a9a;
    --page: #efefef;
    --white: #ffffff;
    --line: #dcdcdc;
    --footer: #3b3b3b;
    --black-btn: #1c1c1c;
  }
  * { box-sizing: border-box; margin: 0; padding: 0; }
  html, body { width: 1200px; height: 2426px; overflow: hidden; }
  body { font-family: "Open Sans", Arial, sans-serif; background: var(--page); color: var(--text); position: relative; }
  .accent { color: var(--red); font-weight: 600; }
  .strong { font-weight: 700; color: var(--ink); }

  /* header */
  .site-header { position: absolute; top: 0; left: 0; width: 1200px; height: 81px; background: #f6f6f6; border-top: 4px solid var(--red); }
  .brand { position: absolute; left: 157px; top: 20px; display: flex; align-items: center; gap: 10px; }
  .brand-mark { width: 36px; height: 36px; border-radius: 50%; background: var(--red); }
  .brand-name { font-size: 24px; font-weight: 600; color: var(--ink); }
  .main-nav { position: absolute; left: 542px; top: 27px; display: flex; gap: 0; }
  .main-nav a { display: block; height: 37px; line-height: 35px; padding: 0 20px; font-size: 12px; color: #444; text-decoration: none; border: 1px solid transparent; }
  .main-nav a.active { border-color: var(--line); background: var(--white); }
  .auth { position: absolute; left: 844px; top: 26px; display: flex; gap: 6px; }
  .auth a { display: block; height: 39px; line-height: 39px; padding: 0 24px; color: var(--white); font-size: 14px; font-weight: 600; text-decoration: none; }
  .btn-login { background: var(--blue); width: 84px; text-align: center; padding: 0 !important; }
  .btn-register { background: var(--red); width: 110px; text-align: center; padding: 0 !important; }

  /* hero */
  .hero { position: absolute; top: 81px; left: 0; width: 1200px; height: 440px; overflow: hidden;
    background: radial-gradient(ellipse at 70% 20%, #c08a55 0%, transparent 45%), linear-gradient(180deg, #6f6a66 0%, #47607b 45%, #2e5b86 100%); }
  .hero-wedge { position: absolute; left: 0; top: 0; }
  .hero h1 { position: absolute; left: 154px; top: 108px; font-size: 39px; font-weight: 300; color: var(--white); }
  .hero h1 b { font-weight: 700; }
  .hero-rule { position: absolute; left: 154px; top: 170px; width: 430px; height: 1px; background: rgba(255,255,255,.4); }
  .hero p { position: absolute; left: 154px; top: 186px; width: 460px; font-size: 16px; line-height: 22px; color: var(--white); }
  .btn-red { display: inline-block; background: var(--red); color: var(--white); font-size: 16px; text-align: center; text-decoration: none; box-shadow: 0 2px 0 var(--red-dark); }
  .hero .btn-red { position: absolute; left: 157px; top: 270px; width: 110px; height: 30px; line-height: 30px; }
  .hero-figure { position: absolute; left: 700px; top: 60px; width: 350px; height: 350px; border-radius: 40% 40% 30% 30%; background: radial-gradient(circle, rgba(245,245,245,.85) 0%, rgba(220,220,220,.4) 60%, transparent 72%); }
  .carousel-dots { position: absolute; left: 982px; top: 408px; display: flex; gap: 3px; }
  .carousel-dots span { width: 10px; height: 10px; background: var(--red); }
  .carousel-dots span.on { background: var(--white); }

  /* about */
  .about { position: absolute; top: 521px; left: 0; width: 1200px; height: 530px; background: var(--page); }
  .section-title { font-size: 32px; font-weight: 400; color: var(--red); }
  .section-title b { color: var(--ink); font-weight: 700; }
  .about .section-title { position: absolute; left: 154px; top: 42px; }
  .about-slash { position: absolute; left: 470px; top: 45px; }
  .about-photo { position: absolute; left: 178px; top: 102px; width: 250px; height: 428px; border-radius: 110px 110px 0 0; background: linear-gradient(180deg, #7a5a46 0%, #7a5a46 18%, #a9c8e4 30%, #8fb3d6 75%, #e6d8c0 90%); }
  .about-copy { position: absolute; left: 548px; top: 50px; width: 490px; font-size: 14.5px; line-height: 18px; color: var(--text); }
  .about-copy p + p { margin-top: 18px; }
  .audience { position: absolute; left: 548px; top: 380px; display: flex; }
  .audience-item { width: 146px; font-size: 12px; color: #444; }
  .audience-item svg { display: block; margin: 0 0 10px 12px; }
  .audience-item.active { color: var(--red); }
  .audience-item.active span { border-bottom: 1px solid var(--red); padding: 0 8px 6px; }
  .about .btn-red { position: absolute; left: 548px; top: 472px; width: 110px; height: 31px; line-height: 31px; }

  /* services */
  .services { position: absolute; top: 1051px; left: 0; width: 1200px; height: 615px;
    background: radial-gradient(ellipse at 50% 30%, #5c4a38 0%, #2f2820 55%, #1d1914 100%); }
  .services h2 { position: absolute; top: 28px; width: 1200px; text-align: center; font-size: 32px; font-weight: 400; color: var(--white); }
  .services h2 b { font-weight: 700; }
  .services .lead { position: absolute; top: 83px; left: 310px; width: 580px; text-align: center; font-size: 13.5px; line-height: 19px; color: #cfc8bf; }
  .service-card { position: absolute; background: var(--white); text-align: center; }
  .service-card .icon-area { height: 113px; display: flex; align-items: center; justify-content: center; border-bottom: 3px solid var(--red); }
  .service-card h3 { font-size: 21px; font-weight: 600; color: #555; margin-top: 26px; }
  .service-card p { font-size: 11.5px; line-height: 17px; color: #777; margin: 14px auto 0; width: 205px; }
  .service-card .btn-dark, .service-card .btn-accent { position: absolute; left: 64px; width: 121px; height: 33px; line-height: 33px; font-size: 14px; font-weight: 600; color: var(--white); text-decoration: none; display: flex; }
  .btn-dark { background: var(--black-btn); }
  .btn-accent { background: var(--red); }
  .btn-dark i, .btn-accent i { width: 24px; font-style: normal; font-size: 12px; border-right: 1px solid rgba(255,255,255,.25); }
  .btn-dark span, .btn-accent span { flex: 1; }
  .card-organize { left: 218px; top: 159px; width: 254px; height: 362px; }
  .card-visualize { left: 472px; top: 142px; width: 256px; height: 397px; box-shadow: 0 0 12px rgba(0,0,0,.25); z-index: 1; }
  .card-visualize .icon-area { height: 130px; border-bottom-color: var(--black-btn); }
  .card-collaborate { left: 728px; top: 159px; width: 254px; height: 362px; }
  .card-organize .btn-dark, .card-collaborate .btn-dark { top: 304px; }
  .card-visualize .btn-accent { top: 312px; left: 67px; }

  /* how */
  .how { position: absolute; top: 1666px; left: 0; width: 1200px; height: 323px; border-bottom: 1px solid var(--line); }
  .how .section-title { position: absolute; left: 151px; top: 34px; }
  .how-copy { position: absolute; left: 154px; top: 84px; width: 880px; font-size: 14.5px; line-height: 18px; }
  .how-copy p + p { margin-top: 18px; }

  /* benefits */
  .benefits { position: absolute; top: 1990px; left: 0; width: 1200px; height: 358px; }
  .benefits .section-title { position: absolute; left: 154px; top: 46px; }
  .benefit-box { position: absolute; left: 154px; top: 107px; width: 892px; height: 196px; background: var(--white); border: 1px solid var(--line); }
  .benefit-logo { position: absolute; left: 26px; top: 25px; width: 122px; height: 144px; border: 1px solid var(--line); display: flex; flex-direction: column; align-items: center; justify-content: center; gap: 10px; }
  .benefit-logo .mark { width: 54px; height: 54px; border-radius: 50%; background: var(--red); }
  .benefit-logo .name { font-size: 14px; font-weight: 600; color: var(--ink); }
  .benefit-copy { position: absolute; left: 193px; top: 24px; width: 670px; font-size: 14.5px; line-height: 18px; }
  .benefit-copy p + p { margin-top: 18px; }

  /* footer */
  .site-footer { position: absolute; top: 2348px; left: 0; width: 1200px; height: 78px; background: var(--footer); }
  .copyright { position: absolute; left: 154px; top: 30px; font-size: 12px; color: #d0d0d0; }
  .to-top { position: absolute; left: 578px; top: 16px; width: 46px; height: 46px; border-radius: 50%; background: var(--red); border: 4px solid #555; display: flex; align-items: center; justify-content: center; }
  .social { position: absolute; left: 911px; top: 24px; display: flex; gap: 7px; }
  .social span { width: 29px; height: 29px; border-radius: 50%; border: 2px solid #e0e0e0; }
</style>
</head>
<body>

<header class="site-header">
  <div class="brand"><span class="brand-mark"></span><span class="brand-name">ThreadKove</span></div>
  <nav class="main-nav">
    <a class="active" href="#">HOME</a>
    <a href="#">ABOUT US</a>
    <a href="#">CONTACT US</a>
  </nav>
  <div class="auth">
    <a class="btn-login" href="#">LOGIN</a>
    <a class="btn-register" href="#">REGISTER</a>
  </div>
</header>

<section class="hero">
  <svg class="hero-wedge" width="1200" height="440" viewBox="0 0 1200 440" aria-hidden="true">
    <polygon points="600,440 1200,340 1200,440" fill="#f4f4f4" opacity=".85"/>
  </svg>
  <div class="hero-figure" role="img" aria-label="White 3D figure in a tie searching with a magnifying glass"></div>
  <h1>Welcome to <b>ThreadKove</b></h1>
  <div class="hero-rule"></div>
  <p>ThreadKove is an on-line system that allows you to enter what you know about a person, event, object, or group. Who are their friends – and who are their enemies?</p>
  <a class="btn-red" href="#">View all</a>
  <div class="carousel-dots"><span></span><span></span><span class="on"></span><span></span><span></span></div>
</section>

<section class="about">
  <h2 class="section-title">What is Thread<b>Kove?</b></h2>
  <svg class="about-slash" width="20" height="50" aria-hidden="true"><line x1="18" y1="2" x2="2" y2="48" stroke="#e8a09a" stroke-width="1.2"/></svg>
  <div class="about-photo" role="img" aria-label="Portrait photo of a smiling man in a light blue shirt with crossed arms"></div>
  <div class="about-copy">
    <p>Have you ever compiled a lot of data about something, but been unable to figure out what it means? Often, the number of people <span class="accent">involved,</span> the number of <span class="accent">events</span> at which they might have met, and the number of common contacts are just too much for a person to track. This can happen when you are trying to understand the players and interests in <span class="accent">current events,</span> or the characters and actions in a novel. It's easy to collect the data, but hard to visualize it or analyze the relationships.</p>
    <p>This is where ThreadKove comes in. ThreadKove allows you to easily visualize <span class="accent">people, events, things, groups,</span> and timelines and to easily see the relationships between them.</p>
    <p>Use <span class="accent">ThreadKove</span> to plot a novel, or to <span class="accent">investiga</span> our favorite conspiracy theory and look for relationships that have eluded the <span class="accent">investigators.</span> Use it to track the causes and results of <span class="accent">historical events</span> – or current ones. Use it to track changing relationships among your friends at <span class="accent">high school</span>. Use it to track the twists and turns of a role-<span class="accent">playing game</span>.</p>
  </div>
  <div class="audience">
    <div class="audience-item">
      <svg width="28" height="24" viewBox="0 0 28 24" aria-hidden="true"><path d="M2 4h10l2 2 2-2h10v16H16l-2 2-2-2H2z" fill="#333"/><line x1="14" y1="6" x2="14" y2="20" stroke="#fff" stroke-width="1"/></svg>
      <span>Historians</span>
    </div>
    <div class="audience-item active">
      <svg width="34" height="30" viewBox="0 0 34 30" aria-hidden="true"><circle cx="17" cy="5" r="4" fill="#333"/><circle cx="7" cy="17" r="3.5" fill="#333"/><circle cx="27" cy="17" r="3.5" fill="#333"/><path d="M12 28v-6h10v6M2 28v-5h10M22 23h10v5" fill="#333"/><line x1="17" y1="9" x2="17" y2="20" stroke="#333" stroke-width="1.5"/></svg>
      <span>Watchdog group</span>
    </div>
    <div class="audience-item">
      <svg width="28" height="30" viewBox="0 0 28 30" aria-hidden="true"><path d="M4 10 Q14 0 24 10 Z" fill="#333"/><circle cx="14" cy="15" r="6" fill="none" stroke="#333" stroke-width="2"/><path d="M5 29 Q14 18 23 29" fill="none" stroke="#333" stroke-width="2"/></svg>
      <span>Civic hackers,</span>
    </div>
  </div>
  <a class="btn-red" href="#">View all</a>
</section>

<section class="services">
  <h2>our <b>Services</b></h2>
  <p class="lead">ThreadKove is an on-line system that allows you to enter what you know about a person, event, object, or group. Who are their friends and who are their enemies?</p>

  <article class="service-card card-organize">
    <div class="icon-area">
      <svg width="64" height="64" viewBox="0 0 64 64" aria-hidden="true">
        <circle cx="32" cy="9" r="7" fill="#222"/><rect x="22" y="16" width="20" height="12" rx="3" fill="#222"/>
        <path d="M32 28v8M10 36h44M10 36v6M32 36v6M54 36v6" stroke="#222" stroke-width="2" fill="none"/>
        <circle cx="10" cy="48" r="5" fill="#222"/><circle cx="32" cy="48" r="5" fill="#222"/><circle cx="54" cy="48" r="5" fill="#222"/>
        <rect x="3" y="53" width="14" height="8" rx="2" fill="#222"/><rect x="25" y="53" width="14" height="8" rx="2" fill="#222"/><rect x="47" y="53" width="14" height="8" rx="2" fill="#222"/>
      </svg>
    </div>
    <h3>Organize</h3>
    <p>ThreadKove is an on-line system that allows you to enter what you know abut a person event, object, or group, Who are their friends-and who are their enemies? Where have they been, and when were they there..</p>
    <a class="btn-dark" href="#"><i>›</i><span>View all</span></a>
  </article>

  <article class="service-card card-visualize">
    <div class="icon-area">
      <svg width="90" height="50" viewBox="0 0 90 50" aria-hidden="true"><path d="M3 25 Q45 -12 87 25 Q45 62 3 25 Z" fill="none" stroke="#111" stroke-width="4"/><circle cx="45" cy="25" r="13" fill="#111"/><circle cx="45" cy="25" r="5" fill="#fff"/></svg>
    </div>
    <h3>Vistualize</h3>
    <p>Once data has been entered, Use ThreadKove's graphical analysis tools to analyze your data in new ways.</p>
    <a class="btn-accent" href="#"><i>»</i><span>View all</span></a>
  </article>

  <article class="service-card card-collaborate">
    <div class="icon-area">
      <svg width="76" height="62" viewBox="0 0 76 62" aria-hidden="true">
        <circle cx="22" cy="10" r="9" fill="#1a1a1a"/><path d="M10 22h24l6 24H30v14h-6V46h-4v14h-6V46H4z" fill="#1a1a1a"/>
        <circle cx="54" cy="10" r="9" fill="#1a1a1a"/><path d="M42 22h24l6 24H62v14h-6V46h-4v14h-6V46H36z" fill="#1a1a1a"/>
      </svg>
    </div>
    <h3>Colaborate</h3>
    <p>Join with others</p>
    <a class="btn-dark" href="#"><i>»</i><span>View all</span></a>
  </article>
</section>

<section class="how">
  <h2 class="section-title">How does Thread<b style="color:var(--red);font-weight:400">Kove</b> work?</h2>
  <div class="how-copy">
    <p>ThreadKove is an on-line system that allows you to enter what you know about a person, event, object, or group. Who are their friends – and who are their enemies? Where have they been, and when were they there? Who have they met? What have they owned? With whom do they associate? All these can be entered in a simple form that allows you to maintain and update information as it becomes known.</p>
    <p>Once data has been entered, use ThreadKove's graphical analysis tools to ana lyze your data in new ways. Use relationship maps to find out how two people or groups are associated. Use timeline analysis to show cause and effect of seemingly unrelated events. Use social network mapping to show how relationships change over time. Look for events that stand out or relationships that have great impact on multiple events. Like a spider's web, look for the intersections that matter, then look for the players that brought that intersection into focus.</p>
  </div>
</section>

<section class="benefits">
  <h2 class="section-title">What do I get with <b>ThreadKove?</b></h2>
  <div class="benefit-box">
    <div class="benefit-logo"><span class="mark"></span><span class="name">ThreadKove</span></div>
    <div class="benefit-copy">
      <p>Basic ThreadKove will allow any registered user to create, maintain and analyze one investigation. Advanced features will be available a la carte and will include special analytical reports, multiple investigations, and the ability to share an investigation among multiple users. Investigations of general interest could also be shared publicly in read-only mode.</p>
      <p>You will also get access to several read-only public investigations to use as a model. These might include the plots of popular novels or movies, the details of a major political event, or an investigation into a famous crime.</p>
    </div>
  </div>
</section>

<footer class="site-footer">
  <p class="copyright">Copyright 2014, ThreadKove Inc.</p>
  <a class="to-top" href="#" aria-label="Back to top">
    <svg width="18" height="12" viewBox="0 0 18 12" aria-hidden="true"><path d="M2 10 L9 3 L16 10" fill="none" stroke="#fff" stroke-width="3"/></svg>
  </a>
  <div class="social"><span></span><span></span><span></span><span></span></div>
</footer>

</body>
</html>
```